Natural Skincare Product Labels Design

We are looking for a designer to create elegant but quirky, functional product labels for our natural skincare range.
The labels must reflect our brand’s values of simplicity, luxury, and the natural, handmade essence of our products.
https://www.pictogrove.com/marvellaskincare
1. Key Details
Packaging Dimensions
Container Types: Transparent jars.
Sizes for Body Products:
Diameter: 64mm–68mm.
Heights: 80mm, 88mm, and 97mm (lid height: 15mm).
Sizes for Face Creams:
Diameter: 60mm.
Height: 50mm (lid height: 15mm).
Label Fit: For body products, ideally one label size to fit all jar sizes.
For the smaller face cream jars, a separate, tailored label is required.
2. Label Placement
Options include a wrapped-around label or a combination of wrapped-around and top-of-jar elements.
Transparent jars mean the label must leave space for the product to be visible (e.g., partial wrap or cutout areas).
3. Content Requirements
Product Name: Prominently displayed.
Ingredient List: Dedicated space required.
Disclaimer/Usage Instructions: Include space for this information.
4. Design Goals
Look & Feel: Simple, upmarket, and natural, with a handmade essence.
Logo Usage: Our logo is finalized and available in gold, black, and white variants. Use Josefin Bold font for the logo if adjustments are required.
Color Palette: Neutral tones (e.g., whites, blacks, golds) are preferred, with flexibility for subtle pops of color tied to each product’s main ingredient.
5. Imagery
Open to including images and colours (e.g., botanical illustrations) that highlight the main ingredient (e.g., coffee beans, turmeric root, or honeycomb). Also open to labels having a prominent colour to tie it in to the main ingredient.
Alternatively, no images can also work for a clean design.
6. Current Design Context
Our temporary design features gold leaf on top and a simple handmade side label. We’re seeking to elevate this to a more polished, cohesive design.
7. Product Line
- Body Products (Larger Jars)
Tolo Body Butter
Key Ingredients: Guarana & Cupuaçu butter (inspired by Brazil).
Note: “Tolo” is slang for “bum.”
Manuka Honey Body Butter
Key Ingredients: Manuka honey (from New Zealand) & Cupuaçu butter.
Coffee Body Scrub
Key Ingredients: Coffee and Demerara sugar.
Whipped Body Soap - Turmeric
Key Ingredients: Turmeric and Bentonite clay.
Whipped Body Soap - Banana
- Face Products (Smaller Jars)
Face Cream
Key Ingredients: Carrot Oil and Raspberry Oil.
Features natural UV protection.
Good Night Cream
Key Ingredients: Enriched with Magnesium.
Promotes relaxation and restful sleep.
8. Submission Guidelines
Flexibility: Design should allow for consistent branding across all products while accommodating the varying jar sizes and ingredient focus.
Material Considerations: Labels should complement the transparent jars and allow the product inside to remain partially visible.
Print Elements: Incorporating gold accents is a plus but should not overpower the design.
We’re excited to see your vision for a label that celebrates the natural beauty and high quality of our skincare range. Please include mockups to showcase the design in use, particularly on transparent jars of varying sizes.
women 20-50 years of age

```html
<!DOCTYPE html>
<html lang="en">
<head>
<meta charset="utf-8">
<title>Marvella Natural Skincare – Product Labels</title>
<link href="https://fonts.googleapis.com/css2?family=Josefin+Sans:wght@300;400;600;700&family=Montserrat:wght@400;500;600&display=swap" rel="stylesheet">
<style>
  :root {
    --bg: #e8e8e8;
    --label: #ffffff;
    --gold: #c0922f;
    --ink: #111111;
    --muted: #333333;
    --honey: #c0922f;
    --tolo: #cc22ee;
    --coffee: #b5531f;
  }
  * { box-sizing: border-box; margin: 0; padding: 0; }
  html, body { width: 720px; height: 1200px; overflow: hidden; }
  body {
    background: var(--bg);
    display: flex;
    flex-direction: column;
    justify-content: space-evenly;
    align-items: center;
    font-family: "Montserrat", sans-serif;
  }
  .label {
    width: 642px;
    height: 229px;
    background: var(--label);
    display: flex;
    align-items: center;
  }
  .label__front {
    width: 346px;
    display: flex;
    flex-direction: column;
    align-items: center;
    text-align: center;
    padding-left: 8px;
  }
  .brand {
    display: flex;
    flex-direction: column;
    align-items: center;
    margin-bottom: 12px;
  }
  .brand__name {
    font-family: "Josefin Sans", sans-serif;
    font-weight: 400;
    font-size: 21px;
    letter-spacing: 5px;
    color: var(--gold);
    padding-left: 5px;
  }
  .brand__tagline {
    font-family: "Josefin Sans", sans-serif;
    font-size: 7px;
    letter-spacing: 2px;
    color: var(--gold);
    margin-top: 5px;
  }
  .product-title {
    font-family: "Josefin Sans", sans-serif;
    font-weight: 600;
    font-size: 23px;
    line-height: 21px;
    color: var(--ink);
    letter-spacing: 0.5px;
  }
  .product-rule {
    width: 260px;
    height: 3px;
    margin: 6px 0 10px;
    background: var(--accent);
  }
  .product-key {
    font-family: "Josefin Sans", sans-serif;
    font-weight: 300;
    font-size: 12.5px;
    line-height: 15.5px;
    letter-spacing: 0.6px;
    color: var(--muted);
  }
  .label__back {
    flex: 1;
    display: flex;
    flex-direction: column;
    align-items: center;
    text-align: center;
    padding-right: 36px;
  }
  .info__heading {
    font-weight: 500;
    font-size: 11.5px;
    letter-spacing: 0.4px;
    color: var(--gold);
  }
  .info__text {
    font-size: 11.5px;
    line-height: 13.2px;
    color: var(--ink);
    width: 228px;
    margin-bottom: 12px;
  }
  .badges {
    display: flex;
    align-items: center;
    gap: 8px;
    margin-top: 10px;
  }
  .badges__volume {
    font-weight: 600;
    font-size: 9.5px;
    color: var(--gold);
    margin-right: 8px;
  }
  .badge {
    width: 36px;
    height: 36px;
    border: 2px solid var(--gold);
    border-radius: 50%;
  }
  .badge--square { border-radius: 4px; width: 30px; height: 30px; margin-right: 6px; }
  .label--honey { --accent: var(--honey); }
  .label--tolo { --accent: var(--tolo); }
  .label--coffee { --accent: var(--coffee); }
</style>
</head>
<body>

<section class="label label--honey">
  <div class="label__front">
    <div class="brand">
      <span class="brand__name">MARVELLA</span>
      <span class="brand__tagline">NATURAL SKINCARE</span>
    </div>
    <h2 class="product-title">MANUKA HONEY<br>BODY BUTTER</h2>
    <div class="product-rule"></div>
    <p class="product-key">MANUKA HONEY<br>&amp; CUPUAÇU BUTTER</p>
  </div>
  <div class="label__back">
    <h3 class="info__heading">INGREDIENTS:</h3>
    <p class="info__text">Shea butter, cocoa butter, manuka honey, coconut oil, sweet almond oil, jojoba oil, beeswax, vitamin E oil, aloe vera gel, essential oils.</p>
    <h3 class="info__heading">HOW TO USE:</h3>
    <p class="info__text">Apply to dry skin, massage gently, and let it absorb</p>
    <div class="badges">
      <span class="badges__volume">200ML</span>
      <span class="badge badge--square"></span>
      <span class="badge"></span>
      <span class="badge"></span>
      <span class="badge"></span>
    </div>
  </div>
</section>

<section class="label label--tolo">
  <div class="label__front">
    <div class="brand">
      <span class="brand__name">MARVELLA</span>
      <span class="brand__tagline">NATURAL SKINCARE</span>
    </div>
    <h2 class="product-title">TOLO<br>BODY BUTTER</h2>
    <div class="product-rule"></div>
    <p class="product-key">GUARANA &amp;<br>CUPUAÇU BUTTER</p>
  </div>
  <div class="label__back">
    <h3 class="info__heading">INGREDIENTS:</h3>
    <p class="info__text">Shea butter, cocoa butter, cupuaçu butter, guarana extract, coconut oil, sweet almond oil, jojoba oil, beeswax, vitamin E oil, essential oils</p>
    <h3 class="info__heading">HOW TO USE:</h3>
    <p class="info__text">Apply to dry skin, massage gently, and let it absorb</p>
    <div class="badges">
      <span class="badges__volume">200ML</span>
      <span class="badge badge--square"></span>
      <span class="badge"></span>
      <span class="badge"></span>
      <span class="badge"></span>
    </div>
  </div>
</section>

<section class="label label--coffee">
  <div class="label__front">
    <div class="brand">
      <span class="brand__name">MARVELLA</span>
      <span class="brand__tagline">NATURAL SKINCARE</span>
    </div>
    <h2 class="product-title">COFFEE<br>BODY SCRUB</h2>
    <div class="product-rule"></div>
    <p class="product-key">COFFEE AND<br>DEMERARA SUGAR</p>
  </div>
  <div class="label__back">
    <h3 class="info__heading">INGREDIENTS:</h3>
    <p class="info__text">Ground coffee, demerara sugar, coconut oil, sweet almond oil, vitamin E oil, essential oils.</p>
    <h3 class="info__heading">HOW TO USE:</h3>
    <p class="info__text">Apply to wet skin, massage gently, rinse thoroughly.</p>
    <div class="badges">
      <span class="badges__volume">200ML</span>
      <span class="badge badge--square"></span>
      <span class="badge"></span>
      <span class="badge"></span>
      <span class="badge"></span>
    </div>
  </div>
</section>

</body>
</html>
```